Concrete Construction page for marketing my business

I need a nice website where I can upload photos of current work, at the moment I am using linkwall but I would like to have my own webpage, I would need a nice and easy menu at the top of the page

you can find my linkwall page here https://www.linkwall.example/TarvenGroup

For images and ideas...

My Linkwall page is

www.linkwall.example/tarvengroupadelaide/

```html
<!DOCTYPE html>
<html lang="en">
<head>
<meta charset="utf-8">
<title>Tarven Group – Concrete Adelaide</title>
<link href="https://fonts.googleapis.com/css2?family=Chakra+Petch:wght@600;700&family=Roboto:wght@400;500;700&display=swap" rel="stylesheet">
<style>
:root{
  --orange:#f15a1f;
  --dark:#1e1e1e;
  --ink:#222;
  --muted:#666;
  --white:#fff;
  --grey:#cfcfcf;
}
*{box-sizing:border-box;margin:0;padding:0}
html,body{width:1200px;height:3914px;overflow:hidden}
body{position:relative;font-family:"Roboto",sans-serif;color:var(--ink);background:var(--white)}
.abs{position:absolute}
.display{font-family:"Chakra Petch",sans-serif;font-weight:700;letter-spacing:1px}
.btn{position:absolute;display:flex;align-items:center;justify-content:center;gap:8px;background:var(--orange);color:#fff;font-weight:700;font-size:15px;text-transform:uppercase}
.arrow-dot{width:14px;height:14px;border-radius:50%;background:#fff;display:inline-block;position:relative}
.arrow-dot::after{content:"";position:absolute;left:4px;top:3.5px;border:3.5px solid transparent;border-left:5px solid var(--orange)}
.kicker{color:var(--orange);font-weight:500;font-size:21px;letter-spacing:.5px;text-transform:uppercase}
.photo{position:absolute}

/* header */
.topbar{left:475px;top:0;width:725px;height:40px;background:var(--dark);border-bottom-left-radius:40px;color:#fff;font-size:15px;font-weight:500}
.topbar span{position:absolute;top:11px}
.social-dot{position:absolute;top:13px;width:13px;height:13px;border-radius:50%;border:2px solid #fff}
.brand-name{font-family:"Roboto",sans-serif;font-weight:700;white-space:nowrap}
.brand-header{left:110px;top:46px;font-size:32px;line-height:36px;color:var(--dark)}
.brand-footer{left:110px;top:3720px;font-size:30px;line-height:34px;color:#ddd}
.nav{top:72px;font-size:14.5px;font-weight:500;color:var(--dark)}
.nav.active{color:var(--orange)}

/* hero */
.hero{left:0;top:122px;width:1200px;height:650px;background:linear-gradient(180deg,#5a6a66 0%,#4b5560 30%,#3c4a62 60%,#555c6c 100%);clip-path:polygon(0 0,100% 0,100% 508px,50% 650px,0 508px)}
.hero-title{left:0;width:1200px;top:302px;text-align:center;color:#fff;font-size:47px;line-height:52px;text-shadow:0 2px 8px rgba(0,0,0,.5)}
.dot{position:absolute;top:691px;width:13px;height:13px;border-radius:50%;background:#fff}

/* about */
.about-text{left:666px;width:422px;font-size:14.5px;line-height:26px;color:var(--muted)}
.badge{left:270px;top:977px;width:158px;height:119px;background:var(--orange);color:#fff;text-align:center}

/* services */
.services{left:0;top:1345px;width:1200px;height:615px;background:radial-gradient(ellipse at center,#e6e6e6 0%,#cbcbcb 70%,#bdbdbd 100%)}
.card{position:absolute;top:1507px;width:311px;height:378px;background:#fff;box-shadow:0 2px 6px rgba(0,0,0,.15);text-align:center}
.card .photo{left:0;top:0;width:311px;height:203px}
.card .icon{position:absolute;left:123px;top:171px;width:64px;height:64px;border-radius:50%;background:var(--orange);border:3px solid #fff}
.card h3{position:absolute;top:243px;width:100%;font-size:19px;font-weight:500;color:var(--dark)}
.card p{position:absolute;top:276px;left:20px;right:20px;font-size:14.5px;line-height:24px;color:var(--muted)}
.card .more{position:absolute;top:345px;width:100%;display:flex;justify-content:center;align-items:center;gap:7px;color:var(--orange);font-weight:700;font-size:13.5px}
.card .more .arrow-dot{background:var(--orange)}
.card .more .arrow-dot::after{border-left-color:#fff}
.card.active{border-bottom:5px solid var(--orange)}

/* projects */
.tile{position:absolute;border-radius:6px}

/* quote */
.quote{left:0;top:2872px;width:1200px;height:740px;background:linear-gradient(180deg,#f16224,#ee5a1d)}
.contact-item{position:absolute;top:3005px;color:#fff;font-size:15px;line-height:24px}
.contact-item b{display:block;font-size:16.5px;font-weight:700}
.field{position:absolute;background:#fff;border-radius:3px;color:#999;font-size:14px;padding:16px 20px}

/* footer */
.footer-band{left:0;top:3445px;width:1200px;height:469px;background:var(--dark);clip-path:polygon(0 165px,50% 0,100% 165px,100% 100%,0 100%)}
.footer-line{left:0;top:3445px;width:1200px;height:190px;background:#fff;clip-path:polygon(0 152px,50% -14px,100% 152px,100% 165px,50% 0,0 165px)}
.fhead{position:absolute;top:3628px;color:#fff;font-weight:700;font-size:18px}
.fhead::after{content:"";position:absolute;left:0;top:30px;width:60px;height:2px;background:var(--orange)}
.flink{position:absolute;color:#ddd;font-size:12.5px}
.fcircle{position:absolute;width:24px;height:24px;border-radius:50%;background:#3a3a3a}
.bottombar{left:0;top:3857px;width:1200px;height:57px;background:#141414;color:#ddd;font-size:13.5px}
</style>
</head>
<body>

<!-- header -->
<div class="abs topbar">
  <svg class="abs" style="left:45px;top:13px" width="14" height="14" viewBox="0 0 24 24"><path fill="#f15a1f" d="M6.6 10.8a15 15 0 006.6 6.6l2.2-2.2c.3-.3.7-.4 1-.2 1.1.4 2.3.6 3.6.6.6 0 1 .4 1 1V20c0 .6-.4 1-1 1A17 17 0 013 4c0-.6.4-1 1-1h3.5c.6 0 1 .4 1 1 0 1.3.2 2.5.6 3.6.1.3 0 .7-.2 1z"/></svg>
  <span style="left:64px">+61 491 570 156</span>
  <svg class="abs" style="left:226px;top:14px" width="16" height="12" viewBox="0 0 16 12"><rect width="16" height="12" rx="1.5" fill="#f15a1f"/><path d="M1 1l7 5 7-5" stroke="#fff" stroke-width="1.4" fill="none"/></svg>
  <span style="left:250px">hello@tarvengroup.example</span>
  <i class="social-dot" style="left:519px"></i>
  <i class="social-dot" style="left:544px"></i>
  <i class="social-dot" style="left:569px"></i>
  <i class="social-dot" style="left:594px"></i>
</div>
<div class="abs brand-name brand-header">Tarven Group</div>
<div class="abs nav active" style="left:466px">HOME</div>
<div class="abs nav" style="left:532px">ABOUT US</div>
<div class="abs nav" style="left:627px">SERVICES</div>
<div class="abs nav" style="left:719px">PROJECTS</div>
<div class="abs nav" style="left:817px">CONTACT</div>
<div class="btn" style="left:918px;top:59px;width:170px;height:45px;font-size:14.5px;font-weight:500">REQUEST A QUOTE</div>

<!-- hero -->
<div class="abs hero" role="img" aria-label="Photo of a new exposed aggregate driveway with rocks and plants in front of a garage"></div>
<h1 class="abs hero-title display">PLAIN &amp; COLOURED<br>CONCRETE FROM LOCAL<br>EXPERTS IN ADELAIDE</h1>
<div class="btn" style="left:509px;top:501px;width:182px;height:50px;font-size:17px;font-weight:500">GET STARTED</div>
<i class="dot" style="left:567px;background:var(--orange)"></i>
<i class="dot" style="left:585px"></i>
<i class="dot" style="left:603px"></i>
<i class="dot" style="left:621px"></i>

<!-- about -->
<div class="photo" style="left:104px;top:814px;width:231px;height:408px;background:linear-gradient(160deg,#7a6a52,#b9b5ad 45%,#a6a7a4)" role="img" aria-label="Photo of a plain concrete path beside a brick house"></div>
<div class="photo" style="left:365px;top:844px;width:230px;height:408px;background:linear-gradient(180deg,#4a4038,#7f7c77 25%,#8b8882 70%,#7e6e5f)" role="img" aria-label="Photo of an exposed aggregate concrete footpath"></div>
<div class="abs badge">
  <div class="display" style="margin-top:28px;font-size:33px;line-height:34px">29+</div>
  <div style="font-size:13.5px;font-weight:700;margin-top:8px">YEARS IN BUSINESS</div>
</div>
<div class="abs kicker" style="left:666px;top:874px">ABOUT US</div>
<h2 class="abs display" style="left:666px;top:902px;font-size:42px;color:var(--dark)">TARVEN GROUP</h2>
<p class="abs about-text" style="top:974px">Lorem ipsum dolor sit amet, consectetur adipiscing elit, sed do eiusmod tempor incididunt ut labore et dolore magna aliqua. Ut enim ad minim veniam, quis nostrud exercitation ullamco laboris nisi ut aliquip ex ea commodo consequat.</p>
<p class="abs about-text" style="top:1085px">Duis aute irure dolor in reprehenderit in voluptate velit esse cillum dolore eu fugiat nulla pariatur.</p>
<div class="btn" style="left:666px;top:1171px;width:159px;height:46px;font-size:14px">LEARN MORE <i class="arrow-dot"></i></div>

<!-- services -->
<div class="abs services" role="img" aria-label="Grey concrete texture background"></div>
<div class="abs kicker" style="left:0;width:1200px;text-align:center;top:1394px">WHAT WE DO</div>
<h2 class="abs display" style="left:0;width:1200px;text-align:center;top:1420px;font-size:42px;color:var(--dark)">OUR SERVICES</h2>

<div class="card" style="left:111px">
  <div class="photo" style="background:linear-gradient(180deg,#6f93c8,#e8e8e6 40%,#4e4e50)" role="img" aria-label="Photo of a concrete driveway in front of a two-storey house"></div>
  <div class="icon"><svg width="58" height="58" viewBox="0 0 58 58"><g fill="none" stroke="#fff" stroke-width="2"><path d="M16 26l13-9 13 9v15H16z"/><rect x="21" y="29" width="16" height="12"/><path d="M21 33h16M21 37h16"/></g></svg></div>
  <h3>Concrete Driveways</h3>
  <p>Lorem ipsum dolor sit amet, consectetur adipiscing elit, sed do eiusmod</p>
  <div class="more">READ MORE <i class="arrow-dot"></i></div>
</div>
<div class="card active" style="left:445px">
  <div class="photo" style="background:linear-gradient(180deg,#56663f,#77777a 35%,#5e5f63)" role="img" aria-label="Photo of an exposed aggregate footpath"></div>
  <div class="icon"><svg width="58" height="58" viewBox="0 0 58 58"><g fill="none" stroke="#fff" stroke-width="2"><path d="M18 38c8 0 4-10 12-10s4-8 10-8"/><circle cx="18" cy="38" r="3"/><circle cx="40" cy="20" r="3"/></g></svg></div>
  <h3>Concrete Footpaths</h3>
  <p>Lorem ipsum dolor sit amet, consectetur adipiscing elit, sed do eiusmod</p>
  <div class="more">READ MORE <i class="arrow-dot"></i></div>
</div>
<div class="card" style="left:779px">
  <div class="photo" style="background:linear-gradient(160deg,#d8d2c2,#5f5e5c 45%,#4d4c4a)" role="img" aria-label="Photo of exposed aggregate concrete stairs"></div>
  <div class="icon"><svg width="58" height="58" viewBox="0 0 58 58"><path d="M16 40h8v-6h7v-6h7v-6h5" fill="none" stroke="#fff" stroke-width="2"/><path d="M16 40h27" stroke="#fff" stroke-width="2"/></svg></div>
  <h3>Concrete Stairs</h3>
  <p>Lorem ipsum dolor sit amet, consectetur adipiscing elit, sed do eiusmod</p>
  <div class="more">READ MORE <i class="arrow-dot"></i></div>
</div>

<!-- projects -->
<div class="abs kicker" style="left:0;width:1200px;text-align:center;top:2035px">OUR GALLERY</div>
<h2 class="abs display" style="left:0;width:1200px;text-align:center;top:2061px;font-size:42px;color:var(--dark)">RECENT PROJECTS</h2>
<div class="tile" style="left:112px;top:2152px;width:318px;height:310px;background:linear-gradient(180deg,#2f7fd6,#4f7b45 30%,#d1693f 55%,#8a847c)" role="img" aria-label="Photo of steel mesh laid for a concrete slab"></div>
<div class="tile" style="left:112px;top:2473px;width:318px;height:223px;background:linear-gradient(160deg,#5b6b4a,#6f6e6a 55%,#4d5a3e)" role="img" aria-label="Photo of concrete stairs beside garden rocks"></div>
<div class="tile" style="left:441px;top:2152px;width:317px;height:379px;background:linear-gradient(180deg,#151617,#232426)" role="img" aria-label="Photo of a dark exposed aggregate surface"></div>
<svg class="abs" style="left:575px;top:2318px" width="50" height="50" viewBox="0 0 50 50"><circle cx="25" cy="25" r="24" fill="#fff"/><path d="M25 14v22M14 25h22" stroke="#222" stroke-width="3.5"/></svg>
<div class="tile" style="left:441px;top:2541px;width:317px;height:155px;background:linear-gradient(160deg,#7d6a5d,#6e6d6d 45%,#5a5b5e)" role="img" aria-label="Photo of a freshly laid aggregate path"></div>
<div class="tile" style="left:770px;top:2152px;width:318px;height:221px;background:linear-gradient(180deg,#9aa0a8,#4b4e58 30%,#3f4350)" role="img" aria-label="Photo of a dark aggregate driveway"></div>
<div class="tile" style="left:770px;top:2385px;width:318px;height:311px;background:linear-gradient(160deg,#b8ad99,#6b6e3f 15%,#7a7873 40%,#6d6b67)" role="img" aria-label="Photo of an aggregate path beside a fence"></div>
<div class="btn" style="left:506px;top:2743px;width:189px;height:48px;font-size:15px;font-weight:500">VIEW ALL WORKS</div>

<!-- quote -->
<div class="abs quote"></div>
<h2 class="abs display" style="left:0;width:1200px;text-align:center;top:2928px;font-size:42px;color:#fff">REQUEST A FREE QUOTE</h2>
<svg class="abs" style="left:200px;top:3000px" width="52" height="52" viewBox="0 0 52 52"><g fill="none" stroke="#fff" stroke-width="2.2"><path d="M26 40s-12-12-12-21a12 12 0 0124 0c0 9-12 21-12 21z"/><circle cx="26" cy="19" r="4.5"/><path d="M12 38l-6 10h40l-6-10"/></g></svg>
<div class="contact-item" style="left:273px"><b>LOCATION:</b>Adelaide, SA, Australia</div>
<svg class="abs" style="left:470px;top:3000px" width="52" height="52" viewBox="0 0 52 52"><g fill="none" stroke="#fff" stroke-width="2.2"><path d="M14 6l8 10-5 5a26 26 0 0014 14l5-5 10 8-5 7C23 45 7 29 7 11z"/><path d="M30 12a10 10 0 0110 10M30 5a17 17 0 0117 17"/></g></svg>
<div class="contact-item" style="left:543px"><b>PHONE:</b>+61 491 570 156</div>
<svg class="abs" style="left:717px;top:3006px" width="56" height="40" viewBox="0 0 56 40"><g fill="none" stroke="#fff" stroke-width="2.2"><rect x="2" y="2" width="52" height="36" rx="2"/><path d="M2 2l26 20 26-20M2 38l20-18M54 38L34 20"/></g></svg>
<div class="contact-item" style="left:792px"><b>EMAIL:</b>hello@tarvengroup.example</div>

<div class="field" style="left:156px;top:3110px;width:431px;height:50px">Name</div>
<div class="field" style="left:156px;top:3177px;width:431px;height:50px">Email Address</div>
<div class="field" style="left:156px;top:3242px;width:431px;height:50px">Phone Number</div>
<div class="field" style="left:610px;top:3110px;width:435px;height:185px">Message</div>
<div class="btn" style="left:497px;top:3328px;width:206px;height:52px;background:var(--dark);border-radius:3px;font-size:16px">SUBMIT NOW <i class="arrow-dot" style="background:#fff"></i></div>

<!-- footer -->
<div class="abs footer-band"></div>
<div class="abs footer-line"></div>
<div class="abs brand-name brand-footer">Tarven Group</div>

<div class="fhead" style="left:428px">QUICK LINKS</div>
<div class="flink" style="left:434px;top:3685px">Home</div>
<div class="flink" style="left:434px;top:3711px">About Us</div>
<div class="flink" style="left:434px;top:3737px">Services</div>
<div class="flink" style="left:434px;top:3763px">Projects</div>
<div class="flink" style="left:434px;top:3789px">Contact</div>

<div class="fhead" style="left:590px">CONTACT US</div>
<i class="fcircle" style="left:588px;top:3683px"></i><svg class="abs" style="left:594px;top:3689px" width="12" height="12" viewBox="0 0 24 24"><path fill="#fff" d="M6.6 10.8a15 15 0 006.6 6.6l2.2-2.2c.3-.3.7-.4 1-.2 1.1.4 2.3.6 3.6.6.6 0 1 .4 1 1V20c0 .6-.4 1-1 1A17 17 0 013 4c0-.6.4-1 1-1h3.5c.6 0 1 .4 1 1 0 1.3.2 2.5.6 3.6.1.3 0 .7-.2 1z"/></svg>
<div class="flink" style="left:622px;top:3688px">+61 491 570 156</div>
<i class="fcircle" style="left:588px;top:3723px"></i><svg class="abs" style="left:594px;top:3731px" width="12" height="9" viewBox="0 0 16 12"><rect width="16" height="12" rx="1.5" fill="#fff"/><path d="M1 1l7 5 7-5" stroke="#3a3a3a" stroke-width="1.4" fill="none"/></svg>
<div class="flink" style="left:622px;top:3729px">hello@tarvengroup.example</div>
<i class="fcircle" style="left:588px;top:3763px"></i><svg class="abs" style="left:595px;top:3768px" width="10" height="14" viewBox="0 0 10 14"><path fill="#fff" d="M5 14S0 8 0 5a5 5 0 0110 0c0 3-5 9-5 9zm0-7a2 2 0 100-4 2 2 0 000 4z"/></svg>
<div class="flink" style="left:622px;top:3768px">Adelaide, SA, Australia</div>

<div class="fhead" style="left:832px">SUBSCRIBE TO OUR BLOG</div>
<div class="flink" style="left:837px;top:3681px;width:240px;line-height:20px">Sign up today to get resources on how to attract and retain more customers!</div>
<div class="abs" style="left:837px;top:3737px;width:253px;height:36px;background:#fff;border-radius:18px;overflow:hidden">
  <span style="position:absolute;left:14px;top:11px;font-size:11px;color:#888">✉ Email Address</span>
  <div style="position:absolute;right:0;top:0;width:48px;height:36px;background:var(--orange)"><svg style="position:absolute;left:16px;top:10px" width="16" height="16" viewBox="0 0 16 16"><path fill="#fff" d="M15 1L1 7l5 2 2 6z"/></svg></div>
</div>
<i class="abs" style="left:833px;top:3790px;width:30px;height:30px;border-radius:50%;background:#fff"></i>
<i class="abs" style="left:873px;top:3790px;width:30px;height:30px;border-radius:50%;background:var(--orange)"></i>
<i class="abs" style="left:911px;top:3790px;width:30px;height:30px;border-radius:50%;background:#fff"></i>
<i class="abs" style="left:950px;top:3790px;width:30px;height:30px;border-radius:50%;background:#fff"></i>

<div class="abs bottombar">
  <span class="abs" style="left:110px;top:20px">Copyright© 2024 <u>Tarven Group</u> | All Rights Reserved</span>
  <span class="abs" style="left:843px;top:20px">Terms and Conditions &nbsp;|&nbsp; Privacy Policy</span>
</div>

</body>
</html>
```